Vellora - Quality health delivered at your door

Vellora offers home and Community Based Services for adults who wish to continue live independently in their communities. We increase accessibility to health care, reduce health care delivery gap, reduce mortality and morbidity, reduce health while promoting healthy living in the comfort of our patients communities or homes.

We provide on site services and deliver high quality healthcare at your door. Our experienced physicians coordinate care with our certified nurse practitioners and provide chronic care management, physical therapy, rehabilitation and medications management.

Target Market(s)

Older population living in independent living facilities

Industry/Entity Type

Health Care

Contact Information for Business Card

Vellora

Number of Pages Required

4 page

Font styles to use
Sans Serif

Colors

Designer to choose colors to be used in the design.

```html
<!DOCTYPE html>
<html lang="en">
<head>
<meta charset="utf-8">
<title>Vellora - Quality health delivered at your door</title>
<link href="https://fonts.googleapis.com/css2?family=Marcellus&family=PT+Sans:wght@400;700&display=swap" rel="stylesheet">
<style>
:root{
  --green:#435b12;
  --green-dark:#34480c;
  --green-soft:#6d8a2c;
  --orange:#f39a12;
  --tile:#efefef;
  --white:#ffffff;
  --text:#555555;
}
*{box-sizing:border-box;margin:0;padding:0}
html,body{width:1200px;height:3109px;overflow:hidden;background:var(--white)}
body{font-family:"PT Sans",sans-serif;color:var(--text);position:relative}
.page{position:relative;width:1200px;height:3109px;overflow:hidden}
.abs{position:absolute}
.display{font-family:"Marcellus",serif}

/* header */
.brand{left:70px;top:12px;width:150px;text-align:center}
.brand-dot{display:block;width:66px;height:66px;border-radius:50%;background:var(--orange);border:5px solid var(--green);margin:0 auto 6px}
.brand-name{font-family:"Marcellus",serif;font-size:22px;color:var(--green-dark);letter-spacing:1px}
.call{left:640px;top:22px;display:flex;align-items:center;gap:12px}
.call small{display:block;font-size:14px;color:#666}
.call strong{display:block;font-size:25px;color:var(--green);letter-spacing:1px}
.social{display:flex;gap:7px}
.social span{width:56px;height:56px;border-radius:50%;display:block}
.header-social{left:876px;top:24px}
.nav{left:100px;top:114px;display:flex;font-size:14px;color:#555;text-transform:uppercase}
.nav a{display:block;padding:0 11px;line-height:44px;text-decoration:none;color:inherit}
.nav a.active{background:var(--green);color:#fff;padding:0 20px}
.nav-rule{left:0;top:154px;width:1200px;height:2px;background:var(--green)}

/* hero */
.hero-bg{left:0;top:156px;width:1200px;height:520px;background:linear-gradient(100deg,#4e6a1c 0%,#6a8631 45%,#52701f 100%)}
.hero-kicker{left:78px;top:268px;font-style:italic;font-size:22px;color:var(--orange)}
.hero-title{left:78px;top:306px;font-size:38px;line-height:53px;color:#fff;text-transform:uppercase;width:600px}
.btn{display:block;text-align:center;text-transform:uppercase;font-family:"Marcellus",serif;color:#fff;text-decoration:none}
.btn-outline{border:2px solid #fff;font-size:21px;line-height:50px}
.btn-solid{background:var(--green);font-size:22px;line-height:56px;border:2px solid #fff;outline:1px solid var(--green)}
.hero-photo{left:612px;top:282px;width:322px;height:322px;border-radius:50%;border:8px solid #fff;background:radial-gradient(circle at 50% 40%,#9fb7b6,#5f8a78 70%,#3d5a2f)}
.dots{left:1148px;top:328px;display:flex;flex-direction:column;gap:14px}
.dots span{width:17px;height:17px;border-radius:50%;border:2px solid var(--orange)}
.dots span.on{background:var(--orange)}

/* welcome */
.welcome{left:150px;top:728px;width:900px;text-align:center}
.kicker{font-size:18px;color:var(--orange);text-transform:uppercase;font-family:"Marcellus",serif}
.welcome h1{font-size:40px;color:var(--green);font-weight:400;margin:6px 0 22px;letter-spacing:1px}
.welcome p{font-size:13.5px;line-height:23px;color:#666;margin-bottom:8px;padding:0 40px}

/* mission */
.mission-bg{left:0;top:1005px;width:1200px;height:560px;background:linear-gradient(90deg,#4d6a1d,#5c7a27 60%,#4a6619)}
.mission-photo{left:72px;top:1077px;width:480px;height:488px;background:linear-gradient(160deg,#6fa9c7,#3b87b7 50%,#b9c9d2)}
.mission-strip{left:0;top:1487px;width:1200px;height:46px;background:rgba(255,255,255,.12)}
.mission-text{left:543px;top:1140px;width:590px;color:#fff}
.mission-text h2{font-size:38px;font-weight:400;margin:4px 0 18px;letter-spacing:1px}
.mission-text p{font-size:14px;line-height:27px;margin-bottom:6px}
.mission-text .lead{font-size:16px;margin-bottom:10px}

/* services intro */
.svc-band{left:0;top:1606px;width:620px;height:176px;background:var(--orange)}
.svc-band .kicker{position:absolute;left:78px;top:52px;color:#fff;font-size:18px}
.svc-band h2{position:absolute;left:74px;top:80px;font-family:"Marcellus",serif;font-size:40px;font-weight:400;color:var(--green)}
.svc-seal{left:448px;top:1608px;width:174px;height:174px;border-radius:50%;background:var(--orange);border:7px solid var(--green-dark);box-shadow:0 0 0 5px #fff inset}
.svc-intro{left:653px;top:1653px;width:470px;font-size:15px;line-height:25px;color:#666}

/* tiles */
.tile{width:251px;height:250px;background:var(--tile)}
.tile svg{position:absolute;left:75px;top:40px;width:100px;height:100px}
.tile-label{position:absolute;left:0;bottom:0;width:100%;height:64px;background:var(--green);color:#fff;text-transform:uppercase;font-size:15px;line-height:21px;display:flex;align-items:center;justify-content:center;text-align:center;padding:0 30px}
.tile-label.hl{background:var(--orange)}
.ic{fill:var(--green)}
.tile.hot .ic{fill:var(--orange)}

/* footer */
.footer-bg{left:0;top:2673px;width:1200px;height:380px;background:var(--green)}
.footer-seal{left:104px;top:2762px;width:186px;height:186px;border-radius:50%;background:var(--orange);border:8px solid var(--green-dark);box-shadow:0 0 0 4px #fff;display:flex;align-items:center;justify-content:center}
.footer-seal span{font-family:"PT Sans",sans-serif;font-weight:700;font-size:26px;color:#fff}
.footer-social{left:112px;top:2958px}
.footer-social span{width:38px;height:38px;background:var(--orange);border:2px solid #fff}
.fcol{top:2756px;color:#fff;font-size:14px;line-height:25px}
.fcol h3{font-family:"Marcellus",serif;font-weight:400;color:var(--orange);font-size:17px;margin-bottom:14px;text-transform:uppercase}
.fcol ul{list-style:none}
.fcol li::before{content:"";display:inline-block;width:5px;height:5px;border-radius:50%;background:var(--orange);margin:0 14px 3px 2px}
.contact-row{display:flex;gap:18px;margin-bottom:14px}
.contact-row svg{flex:none;width:18px;height:18px;margin-top:4px}
.contact-row b{color:var(--orange);text-transform:uppercase}
.email-input{width:249px;height:44px;background:#f2f2f2;color:#666;font-size:13px;line-height:44px;padding-left:12px;margin-top:14px}
.btn-sub{width:166px;border:2px solid #fff;font-size:19px;line-height:42px;margin-top:16px}
.copy{left:0;top:3046px;width:1200px;height:63px;background:var(--orange);text-align:center;line-height:63px;font-size:14px;color:var(--green-dark)}
.copy b{font-weight:700}
</style>
</head>
<body>
<div class="page">

  <!-- header -->
  <div class="abs brand"><span class="brand-dot"></span><span class="brand-name">VELLORA</span></div>
  <div class="abs call">
    <svg width="42" height="42" viewBox="0 0 24 24"><path fill="#f39a12" d="M6.6 10.8a15 15 0 0 0 6.6 6.6l2.2-2.2a1 1 0 0 1 1-.25 11.4 11.4 0 0 0 3.6.57 1 1 0 0 1 1 1V20a1 1 0 0 1-1 1A17 17 0 0 1 3 4a1 1 0 0 1 1-1h3.5a1 1 0 0 1 1 1c0 1.25.2 2.45.57 3.57a1 1 0 0 1-.25 1z"/></svg>
    <div><small>Call Us On:</small><strong>123 456 7890</strong></div>
  </div>
  <div class="abs social header-social">
    <span style="background:#3b5998"></span><span style="background:#4cb3e6"></span><span style="background:#0e76a8"></span><span style="background:#dd4b39"></span>
  </div>
  <nav class="abs nav">
    <a class="active" href="#">Home</a><a href="#">Assisted Living</a><a href="#">Skilled Nursing</a><a href="#">Independent Living</a><a href="#">Services</a><a href="#">Respite Care</a><a href="#">Rehabilitation</a><a href="#">Norvel Learning Center</a>
  </nav>
  <div class="abs nav-rule"></div>

  <!-- hero -->
  <div class="abs hero-bg" role="img" aria-label="Photo of a caregiver holding an elderly person's hands"></div>
  <div class="abs hero-kicker">WE PROVIDE YOU</div>
  <h1 class="abs hero-title" style="font-family:'PT Sans',sans-serif;font-weight:400">Services and deliver high quality healthcare at your door</h1>
  <a class="abs btn btn-outline" href="#" style="left:78px;top:487px;width:190px">Contact Us</a>
  <svg class="abs" style="left:0;top:600px" width="1200" height="90" viewBox="0 0 1200 90" preserveAspectRatio="none">
    <path d="M0 50 C300 85 650 80 900 40 C1020 22 1120 30 1200 45 V90 H0Z" fill="#f39a12"/>
    <path d="M0 62 C300 95 650 92 900 54 C1020 36 1120 42 1200 58 V90 H0Z" fill="#fff"/>
  </svg>
  <div class="abs hero-photo" role="img" aria-label="Photo of a smiling nurse with an elderly man"></div>
  <div class="abs dots"><span></span><span></span><span></span><span class="on"></span><span></span></div>

  <!-- welcome -->
  <section class="abs welcome">
    <div class="kicker">Welcome to</div>
    <h1 class="display">VELLORA</h1>
    <p>Vellora offers home and Community Based Services for adults who wish to continue to live independently in the comfort of their communities.</p>
    <p>We provide on site services and deliver high quality healthcare at your door. Our experienced physicians coordinate care with our certified nurse practitioners and provide chronic care management, physical therapy, rehabilitation and medications management.</p>
  </section>
  <a class="abs btn btn-solid" href="#" style="left:516px;top:959px;width:166px">Know More</a>

  <!-- mission -->
  <div class="abs mission-bg" role="img" aria-label="Soft green background photo of hands"></div>
  <svg class="abs" style="left:0;top:1004px" width="1200" height="80" viewBox="0 0 1200 80" preserveAspectRatio="none">
    <path d="M0 0 H1200 V10 C900 75 300 75 0 10Z" fill="#fff"/>
  </svg>
  <div class="abs mission-strip"></div>
  <div class="abs mission-photo" role="img" aria-label="Photo of a nurse standing with an elderly woman"></div>
  <section class="abs mission-text">
    <div class="kicker">Our Mission</div>
    <h2 class="display">STATEMENT</h2>
    <p class="lead">We Provide You services and deliver high quality healthcare at your door.</p>
    <p>Lorem Ipsum is the simply dummy text of the printing and typesetting industry. Lorem Ipsum has been the industry's standard dummy text ever since the, when an unknown.</p>
    <p>Lorem Ipsum is simply dummy text of the printing and typesetting industry. Lorem Ipsum has been the industry's standard dummy text ever since the 1500s, when an unknown printer took a galley of type and scrambled it to make a type specimen book.</p>
  </section>
  <a class="abs btn btn-outline" href="#" style="left:543px;top:1423px;width:168px;line-height:52px">Know More</a>

  <!-- services intro -->
  <div class="abs svc-band"><div class="kicker">We provide you</div><h2>OUR BEST SERVICES</h2></div>
  <div class="abs svc-seal"></div>
  <p class="abs svc-intro">Vellora offers home and Community Based Services for adults who wish to continue to live independently in the comfort of their communities.</p>

  <!-- service tiles -->
  <div class="abs tile hot" style="left:77px;top:1844px">
    <svg viewBox="0 0 100 100"><path class="ic" d="M50 62 30 42a11 11 0 0 1 20-10 11 11 0 0 1 20 10Z"/><path class="ic" d="M6 50c8 6 14 18 24 26h18v10H26C16 78 8 66 6 50Zm88 0c-8 6-14 18-24 26H52v10h22c10-8 18-20 20-36Z"/></svg>
    <div class="tile-label hl">Comprehensive Primary Care</div>
  </div>
  <div class="abs tile" style="left:342px;top:1844px">
    <svg viewBox="0 0 100 100"><circle class="ic" cx="50" cy="26" r="18"/><path class="ic" d="M16 92c0-24 14-38 34-38s34 14 34 38Z"/><circle cx="50" cy="74" r="7" fill="#efefef"/></svg>
    <div class="tile-label">Coordination of Speciality Care</div>
  </div>
  <div class="abs tile" style="left:607px;top:1844px">
    <svg viewBox="0 0 100 100"><circle class="ic" cx="50" cy="14" r="9"/><rect class="ic" x="42" y="26" width="16" height="40" rx="6"/><rect class="ic" x="42" y="60" width="7" height="34"/><rect class="ic" x="51" y="60" width="7" height="34"/><path d="M12 46a38 38 0 0 0 76 0" fill="none" stroke="#435b12" stroke-width="3"/></svg>
    <div class="tile-label">Chronic Disease Management</div>
  </div>
  <div class="abs tile" style="left:872px;top:1844px">
    <svg viewBox="0 0 100 100"><path class="ic" d="M50 10 92 44V92H8V44Z"/><path d="M50 78 34 62a9 9 0 0 1 16-8 9 9 0 0 1 16 8Z" fill="#efefef"/></svg>
    <div class="tile-label">Transitional Care</div>
  </div>

  <div class="abs tile" style="left:77px;top:2109px">
    <svg viewBox="0 0 100 100"><rect class="ic" x="18" y="10" width="6" height="22"/><rect class="ic" x="10" y="18" width="22" height="6"/><circle class="ic" cx="66" cy="20" r="10"/><path class="ic" d="M54 34h24l6 30H48Z"/><rect class="ic" x="8" y="66" width="62" height="14" rx="7"/><rect class="ic" x="10" y="86" width="80" height="5"/></svg>
    <div class="tile-label">Skilled Nursing Visits</div>
  </div>
  <div class="abs tile" style="left:342px;top:2109px">
    <svg viewBox="0 0 100 100"><circle class="ic" cx="36" cy="18" r="7"/><circle class="ic" cx="64" cy="18" r="7"/><rect class="ic" x="29" y="28" width="14" height="30" rx="4"/><rect class="ic" x="57" y="28" width="14" height="30" rx="4"/><path d="M8 44c4 20 18 40 36 44M92 44c-4 20-18 40-36 44" fill="none" stroke="#435b12" stroke-width="8" stroke-linecap="round"/></svg>
    <div class="tile-label">Social Services Assessment</div>
  </div>
  <div class="abs tile" style="left:607px;top:2109px">
    <svg viewBox="0 0 100 100"><path class="ic" d="M50 8 96 40l-6 6L50 18 10 46l-6-6Z"/><circle class="ic" cx="34" cy="48" r="8"/><circle class="ic" cx="66" cy="48" r="8"/><rect class="ic" x="26" y="58" width="16" height="34" rx="4"/><rect class="ic" x="58" y="58" width="16" height="34" rx="4"/></svg>
    <div class="tile-label">Home Health Assistance</div>
  </div>
  <div class="abs tile" style="left:872px;top:2109px">
    <svg viewBox="0 0 100 100"><circle class="ic" cx="48" cy="14" r="9"/><path class="ic" d="M40 26h16l10 34H34Z"/><rect class="ic" x="8" y="62" width="84" height="14" rx="7"/><rect class="ic" x="8" y="82" width="84" height="6"/></svg>
    <div class="tile-label">Physical Therapy</div>
  </div>

  <div class="abs tile" style="left:209px;top:2372px">
    <svg viewBox="0 0 100 100"><path class="ic" d="M50 8c22 0 36 16 34 36l8 16h-10v14c0 6-4 8-10 8h-8v12H28V74C18 66 12 54 14 40 16 22 30 8 50 8Z"/></svg>
    <div class="tile-label">Mental Health</div>
  </div>
  <div class="abs tile" style="left:474px;top:2372px">
    <svg viewBox="0 0 100 100"><path class="ic" d="M30 10c10 0 14 6 20 6s10-6 20-6c14 0 20 12 18 26-2 16-8 20-10 34-2 12-4 22-10 22-8 0-6-26-18-26s-10 26-18 26c-6 0-8-10-10-22-2-14-8-18-10-34-2-14 4-26 18-26Z"/></svg>
    <div class="tile-label">Dental Health</div>
  </div>
  <div class="abs tile" style="left:740px;top:2372px">
    <svg viewBox="0 0 100 100"><path class="ic" d="M24 22h52l12 30h6v24H6V52h6Zm6 8-8 22h56l-8-22Z"/><circle cx="22" cy="64" r="6" fill="#efefef"/><circle cx="78" cy="64" r="6" fill="#efefef"/><rect class="ic" x="10" y="76" width="16" height="14" rx="3"/><rect class="ic" x="74" y="76" width="16" height="14" rx="3"/></svg>
    <div class="tile-label">Transportation</div>
  </div>

  <!-- footer -->
  <div class="abs footer-bg"></div>
  <svg class="abs" style="left:0;top:2660px" width="1200" height="60" viewBox="0 0 1200 60" preserveAspectRatio="none">
    <path d="M0 16 C150 0 250 30 420 26 C620 22 700 0 900 14 C1040 24 1120 8 1200 12 V0 H0Z" fill="#fff"/>
    <path d="M0 34 C200 16 320 44 500 38 C700 32 820 18 1000 30 C1100 36 1160 28 1200 26 V60 H0Z" fill="#34480c" opacity=".45"/>
  </svg>
  <div class="abs footer-seal"><span>Vellora</span></div>
  <div class="abs social footer-social"><span></span><span></span><span></span><span></span></div>

  <div class="abs fcol" style="left:346px">
    <h3>Site Map</h3>
    <ul><li>Home</li><li>Assisted Living</li><li>Skilled Nursing</li><li>Independent Living</li><li>Services</li><li>Respite Care</li><li>Rehabilitation</li><li>Norvel LearningCenter</li><li>Norvel Learning</li></ul>
  </div>

  <div class="abs fcol" style="left:609px;width:230px">
    <h3>Contact Us</h3>
    <div class="contact-row"><svg viewBox="0 0 24 24"><path fill="none" stroke="#f39a12" stroke-width="2" d="M12 22s7-7 7-12a7 7 0 0 0-14 0c0 5 7 12 7 12Z"/><circle cx="12" cy="10" r="2.5" fill="#f39a12"/></svg><div><b>Vellora</b><br>101 - Lorem ipsum is simple dummy text of print and type setting industry.</div></div>
    <div class="contact-row"><svg viewBox="0 0 24 24"><path fill="#f39a12" d="M6.6 10.8a15 15 0 0 0 6.6 6.6l2.2-2.2a1 1 0 0 1 1-.25 11.4 11.4 0 0 0 3.6.57 1 1 0 0 1 1 1V20a1 1 0 0 1-1 1A17 17 0 0 1 3 4a1 1 0 0 1 1-1h3.5a1 1 0 0 1 1 1c0 1.25.2 2.45.57 3.57a1 1 0 0 1-.25 1z"/></svg><div>123 456 7890</div></div>
    <div class="contact-row"><svg viewBox="0 0 24 24"><rect x="3" y="5" width="18" height="14" fill="none" stroke="#f39a12" stroke-width="2"/><path d="M3 5l9 8 9-8" fill="none" stroke="#f39a12" stroke-width="2"/></svg><div>info@vellora.com</div></div>
    <div class="contact-row"><svg viewBox="0 0 24 24"><circle cx="12" cy="12" r="9" fill="none" stroke="#f39a12" stroke-width="2"/><path d="M3 12h18M12 3c3 3 3 15 0 18M12 3c-3 3-3 15 0 18" fill="none" stroke="#f39a12" stroke-width="1.5"/></svg><div>www.vellora.com</div></div>
  </div>

  <div class="abs fcol" style="left:872px;width:260px">
    <h3>Newsletter</h3>
    <p>Would you like to receive exclusive access to articles, white papers and our regular monthly newsletter?</p>
    <div class="email-input">Enter Email Id*</div>
    <a class="btn btn-sub" href="#">Subscribe</a>
  </div>

  <div class="abs copy"><b>VELLORA</b> · 2017 All rights reserved.</div>
</div>
</body>
</html>
```